Gold Ridge Workwear Web Design Project

New uploiad DESIGN 2 and DESIGN 3. These are examples of how we want to setup up our secondary pages. Only for layout purposes though. There design is a little to grey for us.
Limit blue colours to three (as per our logo). Other than blue, white should be used. We like to stay away from other colours, especially grey.
Based on the initial concent of our web site, I only like a few elements. These are:
- Header
- Mono coloured logos for brands, which then come to full colour when scrolled across The main brands we want used as examples are CORVANE / STROLIK / OPTARUN / PELTO / DEL MORVAN / FENDLE / SAFEMARK / GTK (Guardline Toolkit Kitting) / Trade Range / Feel free not to use all, depending on how much room you have to work with. Can have a slide with arrow as to see more.
Layout needs to be clean, simple and not confusing. It needs to be of corporate style, since we are a business to business company and not a consumer one. Our brand is an Australian icon and this web site design needs to reflect this. Our main clientelle is Mining, Construction, Transport, Oil & Gas, although our motto is Gear for all, Gear Gold Ridge which is to give the impression that we deal with all and everyone. We can cater to the needs of any business.
Attached is our site map / menu structure. The main titles will go across ways underneath the main header. Then a drop down menu of sorts will show the other titles one down. Any third level menus are only to be links in the pages of second level. We have highlighted featured menu subjects that we think could do with another link on the homepage also to highlight subject. Arrows down on the top level menu is to indicate then menu drops down. I do like this - open to suggestions.
Quick Quote and Industry Partner should be featured links in the main page, without being in the header menu.
Industry partner section would then relate back to the Industry Links - almost being like a header page for the rest of the Industries mentioned under the header bar.
BRANDS would have all the images of Brand under, with a possible small blurb about each one. There would be a left hand column with a menu of sorts
Industry would be set out similar with the left hand column menu, would have a few paragraphs about the industry and how we represent them through workwear, then with three rows across and three to four rows down of images which would be a small showing of what type of uniforms are on offer. No text is needed. Just want them to look clean.
Possible stamp like image - saying: THE GOLD RIDGE DIFFERENCE on the main page.
Socia Media links. Being a business to business company, ProLinker is an important social media link to have. Not so important, but still necessary is Friendspace and Chirpline. VIDTUBA.
Please keep in mind this site is to be an information site only. It's not an ecommerce site, so the web site will show a few images as examples, but nothing too specific about each garment, just an overview as such. There will be a seperate web site setup for a client portal for e-commerce side of things. A Login link and Register link on the main page are required for this. Also a VISIT THE GOLD RIDGE STORE link.
Business to Business - not consumer

```html
<!DOCTYPE html>
<html lang="en">
<head>
<meta charset="utf-8">
<title>Gold Ridge Workwear – Oil &amp; Gas</title>
<link href="https://fonts.googleapis.com/css2?family=ABeeZee&family=Bree+Serif&display=swap" rel="stylesheet">
<style>
:root{
  --navy:#0e3a7a;
  --royal:#1e4fa8;
  --link:#3a74d0;
  --soft-blue:#9fb3d4;
  --mist-blue:#c4d2e8;
  --pale:#eef2f8;
  --faded-text:#b7bfcc;
  --footer:#aabcd8;
  --white:#ffffff;
  --hover-red:#e5a3a6;
}
*{box-sizing:border-box;margin:0;padding:0}
html,body{width:952px;height:1200px;overflow:hidden;background:var(--white)}
body{position:relative;font-family:"ABeeZee",sans-serif;color:var(--faded-text)}
.abs{position:absolute}
.serif{font-family:"Bree Serif",serif}

/* top bar */
.top-bar{left:0;top:0;width:952px;height:28px;background:var(--navy);border-bottom:2px solid var(--royal)}
.top-bar .item{position:absolute;top:7px;color:var(--white);font-size:9.5px}
.top-bar .phone-num{font-size:11px;top:7px}
.top-bar .sep{position:absolute;top:6px;color:var(--white);font-size:10px}

/* header */
.brand{left:142px;top:42px;display:flex;align-items:center;gap:8px}
.brand .mark{width:22px;height:22px;background:var(--navy)}
.brand .name{font-family:"Bree Serif",serif;color:var(--navy);font-size:18px;line-height:1;letter-spacing:.5px}
.main-nav{top:79px;font-family:"Bree Serif",serif;font-size:13.5px;color:#222;letter-spacing:.4px;display:flex;align-items:center;gap:9px}
.main-nav.active{color:var(--royal)}
.nav-rule{left:142px;top:109px;width:670px;height:3px;background:var(--mist-blue)}

/* dropdown */
.dropdown{left:484px;top:110px;width:171px;height:204px;background:var(--white);box-shadow:0 1px 4px rgba(0,0,0,.25);padding:0 14px}
.dropdown .entry{position:absolute;left:14px;width:150px}
.dropdown .title{color:var(--navy);font-size:9.5px;letter-spacing:.3px}
.dropdown .desc{color:var(--link);font-size:7px;line-height:8.5px}

/* breadcrumb */
.breadcrumb{left:142px;top:121px;font-size:9px;color:var(--mist-blue);display:flex;align-items:center;gap:8px}

/* sidebar */
.catalogue-box{left:140px;top:141px;width:158px;height:226px;border:1px solid #e3e7ee;box-shadow:0 1px 2px rgba(0,0,0,.06)}
.catalogue-box .head{height:24px;background:var(--soft-blue);color:var(--white);font-size:10px;text-align:center;line-height:24px}
.catalogue-art{left:21px;top:40px;width:100px;height:80px;background:linear-gradient(135deg,#eef3f8,#c9dbe6);transform:rotate(-8deg)}
.catalogue-box .blurb{position:absolute;left:16px;top:144px;width:130px;font-size:8.5px;line-height:10.5px;color:#d3d8e0}
.btn{background:var(--soft-blue);color:var(--white);text-align:center;border-radius:3px;font-size:9.5px}
.catalogue-box .btn{position:absolute;left:15px;top:188px;width:128px;height:22px;line-height:22px}

/* hero */
.hero{left:326px;top:140px;width:488px;height:249px;background:linear-gradient(180deg,#e6edf3 0%,#dfe6ec 55%,#cfd8e0 100%)}
.hero-caption{left:326px;top:361px;width:488px;height:28px;background:var(--soft-blue);color:var(--white);font-size:12.5px;padding-left:12px;line-height:28px}

/* article */
.page-title{left:326px;top:398px;color:var(--soft-blue);font-size:17.5px;letter-spacing:.3px}
.article{left:326px;top:423px;width:468px;font-size:10.3px;line-height:11.8px;color:var(--faded-text)}
.article p{margin-bottom:11.5px}

/* featured band */
.featured-band{left:0;top:670px;width:952px;height:210px;background:linear-gradient(180deg,var(--pale) 0%,var(--pale) 80%,#ffffff 100%)}
.portal-btn{left:154px;top:680px;width:130px;height:32px;line-height:32px;font-size:10.5px;border-radius:0}
.section-title{color:var(--soft-blue);font-size:16px;letter-spacing:.3px}
.product{top:718px;width:154px;height:168px;background:var(--white);border:1px solid var(--mist-blue)}
.product .shot{position:absolute;left:40px;top:10px;width:74px;height:88px;background:linear-gradient(180deg,#d8e0ec,#b9c7dc);border-radius:4px}
.product .label{position:absolute;left:0;top:107px;width:100%;text-align:center;font-size:10px;line-height:12px;color:#c4c9d2}
.product .btn{position:absolute;left:20px;top:136px;width:112px;height:20px;line-height:20px;font-size:9px;border-radius:4px}

/* brands */
.brands-strip{left:140px;top:933px;width:677px;height:63px;background:var(--white);box-shadow:0 0 6px rgba(0,0,0,.08)}
.brand-tile{top:943px;height:41px;display:flex;align-items:center;justify-content:center;font-family:"Bree Serif",serif;font-size:24px;color:var(--mist-blue);background:var(--pale)}
.brand-tile.hover{color:var(--hover-red);background:#fbeeee}

/* footer */
.footer{left:0;top:1010px;width:952px;height:190px;background:var(--footer)}
.footer .rule{position:absolute;left:142px;width:670px;height:1px;background:#c6d3e6}
.footer h3{position:absolute;font-family:"Bree Serif",serif;font-weight:400;color:var(--white);font-size:15px;letter-spacing:.2px}
.footer .signup-input{position:absolute;left:253px;top:48px;width:194px;height:20px;background:var(--white)}
.footer .signup-text{position:absolute;left:142px;top:77px;width:290px;font-size:8px;line-height:10px;color:var(--white)}
.footer ul{position:absolute;list-style:none;font-size:9px;color:var(--white)}
.footer li{height:17px;display:flex;align-items:center;gap:6px}
.footer .dot{width:6px;height:6px;border-radius:50%;background:var(--white)}
.footer .legal{position:absolute;top:170px;font-size:8.5px;color:var(--white)}
</style>
</head>
<body>

<header>
  <div class="abs top-bar">
    <svg class="abs" style="left:483px;top:3px" width="21" height="21" viewBox="0 0 21 21" aria-hidden="true">
      <circle cx="10.5" cy="10.5" r="9.5" fill="none" stroke="#fff" stroke-width="1.4"/>
      <path d="M7 5.5c-.8.5-1.3 1.4-1 2.6.8 3 3.6 6 6.6 6.8 1.2.3 2.1-.2 2.6-1l-1.8-1.6-1.3.8c-1.5-.6-2.6-1.8-3.2-3.2l.8-1.3z" fill="#fff"/>
    </svg>
    <span class="item phone-num" style="left:513px">1300 555 018</span>
    <span class="sep" style="left:601px">|</span>
    <span class="item" style="left:626px">Catalogues</span>
    <span class="sep" style="left:695px">|</span>
    <span class="item" style="left:716px">Login</span>
    <span class="sep" style="left:757px">|</span>
    <span class="item" style="left:778px">Register</span>
  </div>

  <div class="abs brand">
    <span class="mark"></span>
    <span class="name">GOLD RIDGE WORKWEAR</span>
  </div>

  <nav>
    <div class="abs main-nav" style="left:377px">PRODUCTS <svg width="7" height="8" viewBox="0 0 7 8"><path d="M0 0l7 4-7 4z" fill="#999"/></svg></div>
    <div class="abs main-nav active" style="left:500px">INDUSTRIES <svg width="8" height="7" viewBox="0 0 8 7"><path d="M0 0h8L4 7z" fill="#1e4fa8"/></svg></div>
    <div class="abs main-nav" style="left:631px">MEDIA <svg width="7" height="8" viewBox="0 0 7 8"><path d="M0 0l7 4-7 4z" fill="#999"/></svg></div>
    <div class="abs main-nav" style="left:731px">ABOUT US <svg width="7" height="8" viewBox="0 0 7 8"><path d="M0 0l7 4-7 4z" fill="#999"/></svg></div>
  </nav>
  <div class="abs nav-rule"></div>
</header>

<div class="abs breadcrumb">
  <svg width="13" height="11" viewBox="0 0 13 11"><path d="M6.5 0L0 5.5h2V11h3.5V7.5h2V11H11V5.5h2z" fill="#c4d2e8"/></svg>
  <span>›</span><span>Industries</span><span>›</span><span>Oil &amp; Gas</span>
</div>

<aside class="abs catalogue-box">
  <div class="head">REQUEST A CATALOGUE</div>
  <div class="abs catalogue-art" role="img" aria-label="Open workwear catalogue showing garments on site"></div>
  <p class="blurb">Lorem Ipsum. Proin gravida nibh vel velit auctor aliquet. request a brochure</p>
  <div class="btn">REQUEST A CATALOGUE</div>
</aside>

<div class="abs hero" role="img" aria-label="Oil and gas worker in hi-vis vest and hard hat beside storage tanks"></div>
<div class="abs hero-caption">Nibh vel velit auctor aliquet. Aenean sollicitudin, lorem quis bibendum</div>

<h1 class="abs page-title serif" style="font-weight:400">OIL &amp; GAS WORKWEAR</h1>
<div class="abs article">
  <p>Lorem Ipsum. Proin gravida nibh vel velit auctor aliquet. Aenean sollicitudin, lorem quis bibendum auctor, nisi elit consequat ipsum, nec sagittis sem nibh id elit. Duis sed odio sit amet nibh vulputate cursus a sit amet mauris. Morbi accumsan ipsum velit. Nam nec tellus a odio tincidunt auctor a ornare odio.</p>
  <p>Class aptent taciti sociosqu ad litora torquent per conubia nostra, per inceptos himenaeos. Mauris in erat justo. Nullam ac urna eu felis dapibus condimentum sit amet a augue. Sed non neque elit. Sed ut imperdiet nisi. Proin condimentum fermentum nunc. Etiam pharetra, erat sed fermentum feugiat, velit mauris egestas quam, ut aliquam massa nisl quis neque. Suspendisse in orci enim.</p>
  <p>Lorem Ipsum. Proin gravida nibh vel velit auctor aliquet. Aenean sollicitudin, lorem quis bibendum auctor, nisi elit consequat ipsum, nec sagittis sem nibh id elit. Duis sed odio sit amet nibh vulputate cursus a sit amet mauris. Morbi accumsan ipsum velit. Nam nec tellus a odio tincidunt auctor a ornare odio.</p>
  <p>Class aptent taciti sociosqu ad litora torquent per conubia nostra, per inceptos himenaeos. Mauris in erat justo. Nullam ac urna eu felis dapibus condimentum sit amet a augue. Sed non neque elit. Sed ut imperdiet nisi. Proin condimentum fermentum nunc. Etiam pharetra, erat sed fermentum feugiat, velit mauris</p>
</div>

<div class="abs dropdown">
  <div class="entry" style="top:-5px"><div class="title">BUILDING &amp; CONSTRUCTION</div><div class="desc">Especially designed for the building<br>and construction people</div></div>
  <div class="entry" style="top:27px"><div class="title">MINING &amp; INDUSTRIAL</div><div class="desc">Lorem Ipsum. Proin gravida nibh vel<br>velit auctor aliquet. Aenean</div></div>
  <div class="entry" style="top:60px"><div class="title">OIL &amp; GAS</div><div class="desc">Lorem Ipsum. Proin gravida nibh vel</div></div>
  <div class="entry" style="top:94px"><div class="title">HOSPITALITY</div><div class="desc">Lorem Ipsum. Proin gravida nibh vel<br>velit auctor aliquet. Aenean</div></div>
  <div class="entry" style="top:127px"><div class="title">HEALTH CARE</div><div class="desc">Lorem Ipsum. Proin gravida nibh vel</div></div>
  <div class="entry" style="top:158px"><div class="title">OTHER INDUSTRIES</div><div class="desc">Lorem Ipsum. Proin gravida nibh vel<br>velit auctor aliquet. Aenean</div></div>
</div>

<section>
  <div class="abs featured-band"></div>
  <div class="abs btn portal-btn">PRODUCT PORTAL</div>
  <h2 class="abs section-title serif" style="left:326px;top:686px;font-weight:400">FEATURED PRODUCTS</h2>

  <div class="abs product" style="left:327px">
    <div class="shot" role="img" aria-label="Coverall with reflective trim"></div>
    <div class="label">Coverall with<br>Reflective Trim</div>
    <div class="btn">LEARN MORE</div>
  </div>
  <div class="abs product" style="left:494px">
    <div class="shot" role="img" aria-label="Team jacket"></div>
    <div class="label">Team Jacket</div>
    <div class="btn">LEARN MORE</div>
  </div>
  <div class="abs product" style="left:665px">
    <div class="shot" role="img" aria-label="Insulated bib overall"></div>
    <div class="label">Insulated Bib<br>Overall</div>
    <div class="btn">LEARN MORE</div>
  </div>
</section>

<section>
  <h2 class="abs section-title serif" style="left:157px;top:907px;font-weight:400">OUR TOP BRANDS</h2>
  <div class="abs brands-strip"></div>
  <svg class="abs" style="left:150px;top:947px" width="14" height="34" viewBox="0 0 14 34"><path d="M12 2L2 17l10 15" fill="none" stroke="#c4d2e8" stroke-width="2"/></svg>
  <div class="abs brand-tile" style="left:177px;width:125px">Corvane</div>
  <div class="abs brand-tile" style="left:318px;width:148px">Strolik</div>
  <div class="abs brand-tile hover" style="left:481px;width:150px">PELTO</div>
  <div class="abs brand-tile" style="left:646px;width:135px">OPTARUN</div>
  <svg class="abs" style="left:792px;top:947px" width="14" height="34" viewBox="0 0 14 34"><path d="M2 2l10 15L2 32" fill="none" stroke="#c4d2e8" stroke-width="2"/></svg>
</section>

<footer class="abs footer">
  <div class="rule" style="top:29px"></div>
  <h3 style="left:142px;top:47px">EMAIL SIGNUP</h3>
  <div class="signup-input"></div>
  <p class="signup-text">Sign up and we'll keep you updated with the latest GOLD RIDGE WORKWEAR product updates, news and events</p>

  <h3 style="left:471px;top:47px">SOCIAL</h3>
  <ul style="left:471px;top:72px">
    <li><span class="dot"></span>Blog</li>
    <li><span class="dot"></span>Friendspace</li>
    <li><span class="dot"></span>Chirpline</li>
    <li><span class="dot"></span>Vidtuba</li>
  </ul>

  <h3 style="left:581px;top:47px">EXPLORE</h3>
  <ul style="left:581px;top:72px">
    <li>Products</li><li>Gallery</li><li>Installation</li><li>Technical</li>
  </ul>

  <h3 style="left:700px;top:47px">CONNECT</h3>
  <ul style="left:700px;top:72px">
    <li>Contact</li><li>Brochure</li><li>FAQs</li><li>Downloads</li>
  </ul>

  <div class="rule" style="top:159px"></div>
  <p class="legal" style="left:156px">Copyright © 2012 <strong>GOLD RIDGE WORKWEAR</strong> All Rights Reserved</p>
  <p class="legal" style="left:714px">Privacy Policy</p>
  <p class="legal" style="left:782px">Term of Use</p>
</footer>

</body>
</html>
```